website update

We need to redesign our current website to be more personalised and sophisticated. We are physiotherapy clinic based in sydney australia, offer a range of clinical service such as Physiotherapy, Massage, sports injuries rehabilitation, Women's health (incontinency etc), Pilates classes, back pain exercise program, acupuncture, Gait analysis.
our current website is www.tidewellrehab.com.au
an example of ideal website is http://orchardlanekinetics.com/
homepage: with a revolving displaying attached photos which is linked to relevants page

```html
<!DOCTYPE html>
<html lang="en">
<head>
<meta charset="utf-8">
<title>Tidewell Physiotherapy &amp; Sports Clinic – Home</title>
<link rel="stylesheet" href="https://fonts.googleapis.com/css2?family=Roboto:wght@300;400;500;700&family=Arimo:wght@400&display=swap">
<style>
  :root {
    --green: #77c043;
    --icon-green: #8cc63f;
    --lime: #c8df5d;
    --lime-deep: #b2d548;
    --cyan: #41c4dd;
    --blue: #3399dd;
    --heading-blue: #2d92d8;
    --text-dark: #3f3f3f;
    --text-grey: #888;
    --nav-text: #444;
    --rule: #e2e2e2;
    --frame: #f1f1f1;
    --white: #fff;
  }
  * { box-sizing: border-box; margin: 0; padding: 0; }
  html, body { width: 1200px; height: 1000px; overflow: hidden; background: var(--white); }
  body { position: relative; font-family: "Roboto", Arial, sans-serif; color: var(--text-dark); }

  .review-note {
    position: absolute; left: 15px; top: 296px; width: 176px;
    font-family: "Arimo", Arial, sans-serif; font-size: 21.5px; line-height: 30px; color: #000;
    white-space: nowrap;
  }
  .review-note p + p { margin-top: 30px; }

  .page-frame {
    position: absolute; left: 192px; top: 0; width: 794px; height: 1000px;
    background: repeating-linear-gradient(45deg, var(--frame) 0 2px, #f8f8f8 2px 4px);
  }
  .page {
    position: absolute; left: 208px; top: 10px; width: 764px; height: 990px; background: var(--white);
  }

  /* Header */
  .brand { position: absolute; left: 20px; top: 17px; display: flex; align-items: center; gap: 8px; }
  .brand-mark { width: 50px; height: 50px; border-radius: 50%; background: var(--green); }
  .brand-name { font-size: 26px; font-weight: 700; color: var(--green); line-height: 26px; letter-spacing: -0.5px; }
  .brand-tag { font-size: 7.5px; font-weight: 500; color: #5a5a5a; letter-spacing: 0.3px; margin-top: 2px; }

  .contact-bar { position: absolute; right: 22px; top: 13px; display: flex; gap: 12px; font-size: 8.5px; color: #555; }
  .contact-bar span { display: flex; align-items: center; gap: 4px; }
  .social { position: absolute; right: 19px; top: 40px; display: flex; }
  .social i { width: 20px; height: 20px; border: 1px solid var(--rule); margin-left: -1px; display: block; position: relative; }
  .social i::after { content: ""; position: absolute; left: 6px; top: 6px; width: 6px; height: 6px; background: #bbb; }

  /* Navigation */
  .main-nav { position: absolute; left: 20px; top: 81px; width: 725px; height: 36px; display: flex; border: 1px solid var(--rule); border-left: 0; }
  .main-nav a {
    height: 100%; display: flex; align-items: center; justify-content: center;
    font-size: 9px; font-weight: 500; color: var(--nav-text); text-decoration: none; border-left: 1px solid var(--rule);
  }
  .main-nav a.current { background: var(--green); color: var(--white); border-left: 0; }

  /* Hero */
  .hero {
    position: absolute; left: 20px; top: 127px; width: 727px; height: 375px;
    background: linear-gradient(110deg, #4f5968 0%, #7e8793 40%, #c8ccd2 60%, #9aa0a8 80%, #5e6470 100%);
  }
  .hero-copy { position: absolute; left: 38px; top: 52px; color: var(--white); }
  .hero-title { font-size: 38px; font-weight: 300; color: var(--green); line-height: 40px; }
  .hero-sub { font-size: 25px; font-weight: 300; line-height: 30px; }
  .hero-list { list-style: none; margin-top: 36px; }
  .hero-list li { font-size: 11.5px; letter-spacing: 1px; line-height: 22.6px; display: flex; align-items: center; gap: 10px; }

  /* Info tiles */
  .tiles { position: absolute; left: 20px; top: 502px; width: 727px; height: 195px; display: flex; }
  .tile { width: 182px; padding: 20px 14px; color: var(--white); }
  .tile h2 { font-size: 20px; font-weight: 300; line-height: 23px; margin-bottom: 17px; }
  .tile p { font-size: 9px; line-height: 11.7px; width: 150px; }
  .tile .more { display: block; margin-top: 25px; font-size: 9px; color: var(--white); text-decoration: none; }
  .tile-news { background: var(--lime); }
  .tile-doctors { background: var(--cyan); }
  .tile-service { background: var(--lime-deep); }
  .tile-hours { background: var(--blue); width: 181px; padding-left: 12px; }
  .hours-row { display: flex; justify-content: space-between; font-size: 8.5px; padding: 7px 0; border-bottom: 1px solid rgba(255,255,255,.45); }

  /* Welcome */
  .welcome { position: absolute; left: 20px; top: 728px; width: 727px; text-align: center; }
  .welcome h1 { font-size: 25px; font-weight: 300; color: var(--heading-blue); }
  .welcome p { font-size: 13px; font-weight: 300; color: var(--text-grey); line-height: 19px; margin: 0 12px; }

  /* Features */
  .features { position: absolute; left: 20px; top: 843px; width: 727px; display: flex; justify-content: space-between; }
  .feature { width: 182px; text-align: center; }
  .feature svg { height: 36px; display: block; margin: 0 auto 15px; }
  .feature h3 { font-size: 14px; font-weight: 400; color: #444; margin-bottom: 12px; }
  .feature p { font-size: 7.8px; line-height: 11.5px; color: var(--text-grey); padding: 0 12px; }
</style>
</head>
<body>
  <aside class="review-note">
    <p>text and content<br>can be changed<br>as per you like.</p>
    <p>Please see the<br>layout and design<br>part and let me<br>know so we can<br>improvise further.</p>
  </aside>

  <div class="page-frame"></div>

  <main class="page">
    <header>
      <div class="brand">
        <span class="brand-mark"></span>
        <div>
          <div class="brand-name">tidewell</div>
          <div class="brand-tag">PHYSIOTHERAPY &amp; SPORTS CLINIC</div>
        </div>
      </div>
      <div class="contact-bar">
        <span>
          <svg width="7" height="10" viewBox="0 0 7 10"><rect x="0.5" y="0.5" width="6" height="9" rx="1" fill="none" stroke="#41c4dd"/><rect x="2.5" y="7.5" width="2" height="1" fill="#41c4dd"/></svg>
          Contact us: 02 9000 1234
        </span>
        <span>
          <svg width="10" height="7" viewBox="0 0 10 7"><rect width="10" height="7" fill="#41c4dd"/><path d="M0 0 L5 4 L10 0" fill="none" stroke="#fff" stroke-width="0.8"/></svg>
          info@tidewellrehab.com.au
        </span>
      </div>
      <div class="social" aria-label="Social links"><i></i><i></i><i></i><i></i><i></i></div>
    </header>

    <nav class="main-nav">
      <a class="current" href="#" style="width:78px">HOME</a>
      <a href="#" style="width:78px">ABOUT US</a>
      <a href="#" style="width:125px">COMMON CONDITIONS</a>
      <a href="#" style="width:87px">TREATMENTS</a>
      <a href="#" style="width:129px">SPECIALISED SERVICES</a>
      <a href="#" style="width:144px">WORKPLACE ASSESSMENT</a>
      <a href="#" style="width:84px">CONTACT US</a>
    </nav>

    <section class="hero" role="img" aria-label="Photo of a physiotherapist taking a patient's blood pressure as she lies on a treatment table">
      <div class="hero-copy">
        <div class="hero-title">Full Spectre</div>
        <div class="hero-sub">Treatment</div>
        <ul class="hero-list">
          <li><svg width="8" height="6" viewBox="0 0 8 6"><path d="M1 3 L3 5 L7 1" fill="none" stroke="#41c4dd" stroke-width="1.3"/></svg>Medical Counseling</li>
          <li><svg width="8" height="6" viewBox="0 0 8 6"><path d="M1 3 L3 5 L7 1" fill="none" stroke="#41c4dd" stroke-width="1.3"/></svg>Cardiac Clinyc</li>
          <li><svg width="8" height="6" viewBox="0 0 8 6"><path d="M1 3 L3 5 L7 1" fill="none" stroke="#41c4dd" stroke-width="1.3"/></svg>Pediatric Clinic</li>
          <li><svg width="8" height="6" viewBox="0 0 8 6"><path d="M1 3 L3 5 L7 1" fill="none" stroke="#41c4dd" stroke-width="1.3"/></svg>Gynecological Clinic</li>
          <li><svg width="8" height="6" viewBox="0 0 8 6"><path d="M1 3 L3 5 L7 1" fill="none" stroke="#41c4dd" stroke-width="1.3"/></svg>Laboratory Analysis</li>
          <li><svg width="8" height="6" viewBox="0 0 8 6"><path d="M1 3 L3 5 L7 1" fill="none" stroke="#41c4dd" stroke-width="1.3"/></svg>Diagnosis Clinic</li>
        </ul>
      </div>
    </section>

    <section class="tiles">
      <article class="tile tile-news">
        <h2>Clinic News</h2>
        <p>Cum sociis natoque penatibus et magnis dis parturient montesmus. Pro vel nibh et elit mollis commodo et nec augue tristique sed</p>
        <a class="more" href="#">Read More</a>
      </article>
      <article class="tile tile-doctors">
        <h2>Top Doctors</h2>
        <p>Cum sociis natoque penatibus et magnis dis parturient montesmus. Pro vel nibh et elit mollis commodo et nec augue tristique sed</p>
        <a class="more" href="#">Read More</a>
      </article>
      <article class="tile tile-service">
        <h2>24 Hours<br>Service</h2>
        <p>Cum sociis natoque penatibus et magnis dis parturient montesmus. Pro vel nibh et elit mollis commodo et nec augue tristique sed</p>
        <a class="more" href="#">Read More</a>
      </article>
      <article class="tile tile-hours">
        <h2>Opening Hours</h2>
        <div class="hours-row"><span>Monday - Friday</span><span>8.00 - 17.00</span></div>
        <div class="hours-row"><span>Saturday</span><span>9.30 - 17.30</span></div>
        <div class="hours-row"><span>Sunday</span><span>9.30 - 15.00</span></div>
      </article>
    </section>

    <section class="welcome">
      <h1>Welcome to Tidewell Spinal &amp; Sports physiotherapy clinic</h1>
      <p>offer a range of clinical service such as Physiotherapy, Massage, sports injuries rehabilitation, Women's health (incontinency<br>etc), Pilates classes, back pain exercise program, acupuncture, Gait analysis.</p>
    </section>

    <section class="features">
      <article class="feature">
        <svg viewBox="0 0 40 36" width="40"><path d="M20 35 L4 19 A10 10 0 0 1 20 5 A10 10 0 0 1 36 19 Z" fill="#8cc63f"/><path d="M6 18 H14 L17 12 L21 24 L24 16 L26 18 H34" fill="none" stroke="#fff" stroke-width="1.8" stroke-linejoin="round"/></svg>
        <h3>Cardio Monitoring</h3>
        <p>Vitalis theme functionality that was developed with health and medical websites in thought, with all the must-have features included.</p>
      </article>
      <article class="feature">
        <svg viewBox="0 0 40 40" width="38"><g transform="rotate(45 20 20)"><rect x="12" y="2" width="16" height="36" rx="8" fill="none" stroke="#8cc63f" stroke-width="3"/><path d="M13.5 20 H26.5 V30 A6.5 6.5 0 0 1 13.5 30 Z" fill="#8cc63f"/></g></svg>
        <h3>Medical Treatment</h3>
        <p>A fantastic set of 23 custom shortcodes lets you easily and fast create a highly unique and interactive content for your medical website.</p>
      </article>
      <article class="feature">
        <svg viewBox="0 0 40 36" width="38"><rect x="14" y="2" width="12" height="7" rx="2" fill="none" stroke="#8cc63f" stroke-width="2.5"/><rect x="3" y="8" width="34" height="26" rx="3" fill="#8cc63f"/><circle cx="20" cy="21" r="8" fill="#fff"/><path d="M20 16 V26 M15 21 H25" stroke="#8cc63f" stroke-width="2.5"/></svg>
        <h3>Emergency Help</h3>
        <p>Custom Services post type allows you display a variety of medical services for a large hospital as well as for a small private clinic.</p>
      </article>
      <article class="feature">
        <svg viewBox="0 0 34 40" width="30"><path d="M6 38 V28 C2 24 1 19 2 15 C4 6 11 2 18 2 C27 2 32 9 32 16 L33 22 L30 23 V29 C30 31 28 32 26 32 H22 V38 Z" fill="#8cc63f"/><circle cx="17" cy="15" r="5" fill="#fff"/></svg>
        <h3>Emergency Help</h3>
        <p>Custom Services post type allows you display a variety of medical services for a large hospital as well as for a small private clinic.</p>
      </article>
    </section>
  </main>
</body>
</html>
```